Auto and Home Insurance Quote Letter

I am an insurance agent and i have been mailing out a front back auto and home insurance quotes in black and white to prospects in my area. I would like the letter to be updated with a new look and some new graphics that would help catch the attention of the prospects I am mailing to. Anything that would help the prospect to call my office.

```html
<!DOCTYPE html>
<html lang="en">
<head>
<meta charset="utf-8">
<title>Harbor Insurance Agency – Auto and Home Quote Letter</title>
<link href="https://fonts.googleapis.com/css2?family=Montserrat:wght@400;500;600;700;800&display=swap" rel="stylesheet">
<style>
:root{
  --ink:#2a2a2a;
  --dark:#2b2b2d;
  --mid:#555;
  --band-gray:#bdbdbd;
  --row-alt:#ececec;
  --line:#cfcfcf;
  --paper:#ffffff;
  --bg:#e9e7e3;
}
*{box-sizing:border-box;margin:0;padding:0}
html,body{width:800px;height:1200px;overflow:hidden;background:var(--bg)}
body{font-family:'Montserrat',sans-serif;color:var(--ink);position:relative}
.spread{position:absolute;left:7px;top:326px;width:1272px;height:890px;transform:scale(0.615);transform-origin:0 0;display:flex;gap:12px}
.page{position:relative;width:630px;height:890px;background:var(--paper);box-shadow:0 2px 10px rgba(0,0,0,.25);overflow:hidden}
.header-shape{position:absolute;left:0;top:0;width:630px;height:100px}
.agency-name{position:absolute;left:38px;top:28px;color:#fff;text-align:left}
.agency-name .initials{display:block;font-size:30px;font-weight:500;letter-spacing:3px;padding-left:60px;line-height:1}
.agency-name .full{display:block;font-size:12px;font-weight:500;letter-spacing:.5px;margin-top:6px}
.carrier{position:absolute;right:38px;top:32px;display:flex;align-items:center;gap:6px;font-size:17px;font-weight:700;color:var(--ink)}
.carrier .dot{width:16px;height:16px;border-radius:50%;background:var(--ink)}
.contact{position:absolute;right:38px;text-align:right;font-size:9.5px;line-height:1.2}
.contact p+p{margin-top:14px}
.fields{position:absolute;left:38px;display:flex;gap:18px;font-size:9.5px;line-height:15px}
.fields li{list-style:none;display:flex;align-items:center;gap:7px}
.fields svg{width:8px;height:8px}
.headline{position:absolute;left:38px;top:205px;width:460px;font-size:13px;font-weight:700;line-height:1.3}
.intro{position:absolute;left:38px;top:262px;width:556px;font-size:8.6px;line-height:1.45}
.premium-title{position:absolute;left:38px;top:343px;font-size:13.5px;font-weight:700;line-height:1.4}
.driver{position:absolute;left:36px;top:393px;font-size:13.5px;font-weight:700}
.promo-art{position:absolute;left:415px;top:326px;width:175px;height:92px;border:1.5px solid #2f4f86;background:linear-gradient(180deg,#a9d6ef 0%,#cfe7d0 55%,#f2d64a 100%)}
.quote-table{position:absolute;left:38px;width:556px;border:1px solid #9a9a9a;border-radius:12px 12px 0 0;overflow:hidden;font-size:8.8px}
.quote-table .thead{display:grid;background:var(--dark);color:#fff;font-size:12px;font-weight:600;height:30px;align-items:center}
.quote-table .row{display:grid;height:24px;align-items:center}
.quote-table .row:nth-child(odd){background:var(--row-alt)}
.auto-grid{grid-template-columns:1.4fr 1fr 1fr}
.auto-grid>span:first-child{padding-left:26px}
.auto-grid>span:nth-child(2){text-align:center}
.auto-grid>span:nth-child(3){padding-left:72px}
.bold{font-weight:700}
.six-month{position:absolute;left:38px;top:651px;width:556px;height:56px;border:1px solid #9a9a9a;background:var(--row-alt);font-size:8.8px;display:grid;grid-template-columns:1.4fr 1fr 1fr;align-items:center}
.six-month .label{grid-column:2;text-align:center;line-height:1.2}
.six-month .val{text-align:center;line-height:1.2;padding-right:40px}
.six-month .val b{display:block;margin-bottom:12px}
.disclaimer{position:absolute;left:38px;top:720px;width:556px;font-size:7.3px;line-height:1.42;text-align:justify}
.disclaimer .last{text-align:center;display:block}
.opt-out{position:absolute;left:0;width:630px;top:812px;text-align:center;font-size:7.5px;font-weight:700}
.footer{position:absolute;left:0;bottom:0;width:630px;height:46px}
.footer .call{position:absolute;left:0;top:0;width:260px;height:46px;background:var(--band-gray);font-size:14px;font-weight:700;padding:14px 0 0 38px}
.footer .call span{font-weight:600;margin-left:6px}
.footer .bar{position:absolute;left:228px;top:0;width:402px;height:46px}
.footer .web,.footer .addr{position:absolute;color:#fff;font-size:9.5px;display:flex;align-items:center;gap:8px}
.footer .web{left:258px;top:17px}
.footer .addr{left:420px;top:9px;line-height:1.25}
.footer svg.icon{width:11px;height:11px;flex:none}
/* back page */
.pitch{position:absolute;left:38px;top:185px;width:556px;font-size:10.5px;font-weight:500;line-height:1.6}
.pitch b{font-weight:700}
.example-band{position:absolute;left:0;top:245px;width:630px;height:30px;background:var(--dark);color:#fff;font-size:11.5px;font-weight:500;letter-spacing:.6px;padding:8px 0 0 36px}
.home-facts{position:absolute;left:0;top:287px;width:630px;height:34px;border-top:1.5px solid var(--line);border-bottom:1.5px solid var(--line);display:flex;justify-content:space-between;align-items:center;padding:0 58px 0 54px;font-size:9.5px;font-weight:600}
.home-table{top:347px}
.home-grid{grid-template-columns:1.05fr 1fr}
.home-grid>span:first-child{padding-left:14px}
.home-table .row{height:25px}
.quote-note{position:absolute;left:38px;top:602px;width:280px;font-size:9.5px;line-height:1.3}
.sign-off{position:absolute;left:38px;top:700px;font-size:10px}
.signature{position:absolute;left:40px;top:722px;width:150px;height:46px;background:linear-gradient(90deg,#d9d9d9,#f1f1f1)}
.signer{position:absolute;left:38px;top:792px;font-size:10.5px;line-height:1.45}
.burst{position:absolute;left:350px;top:580px;width:190px;height:190px}
.burst-text{position:absolute;left:350px;top:650px;width:190px;text-align:center;color:#fff}
.burst-text small{display:block;font-size:10.5px;font-weight:600;line-height:1.2}
.burst-text strong{display:block;font-size:24px;font-weight:700;margin-top:4px}
.roof-note{position:absolute;left:345px;top:766px;width:245px;font-size:7.6px;line-height:1.3}
.roof-note h3{font-size:8.4px;font-weight:700;line-height:1.2;margin-bottom:6px}
.roof-note b{display:block;margin-top:6px}
</style>
</head>
<body>
<main class="spread">

  <!-- Front: auto quote -->
  <section class="page page-auto" aria-label="Auto insurance quote letter">
    <svg class="header-shape" viewBox="0 0 630 100" aria-hidden="true"><path d="M0 0H630V35H430C360 35 340 95 270 95H0Z" fill="var(--dark)"/></svg>
    <div class="agency-name"><span class="initials">HIA</span><span class="full">HARBOR INSURANCE AGENCY</span></div>
    <div class="carrier"><span class="dot"></span>Keystone</div>
    <div class="contact" style="top:110px">
      <p>Sample Auto Insurance Quote<br>¡Hablamos Español!</p>
      <p>Harbor Insurance Agency, Inc.<br>Orlando, FL<br>407-555-0182<br>DReyes@keystonecover.com<br>HarborInsAgency.com</p>
    </div>
    <ul class="fields" style="top:122px">
      <li><ul><li><svg viewBox="0 0 8 8"><rect x=".5" y=".5" width="7" height="7" fill="none" stroke="#333"/><path d="M1.8 4l1.5 1.5L6.3 2" fill="none" stroke="#333"/></svg>FullName</li><li><svg viewBox="0 0 8 8"><rect x=".5" y=".5" width="7" height="7" fill="none" stroke="#333"/><path d="M1.8 4l1.5 1.5L6.3 2" fill="none" stroke="#333"/></svg>Address</li><li><svg viewBox="0 0 8 8"><rect x=".5" y=".5" width="7" height="7" fill="none" stroke="#333"/><path d="M1.8 4l1.5 1.5L6.3 2" fill="none" stroke="#333"/></svg>Address2</li></ul></li>
      <li><ul><li><svg viewBox="0 0 8 8"><rect x=".5" y=".5" width="7" height="7" fill="none" stroke="#333"/><path d="M1.8 4l1.5 1.5L6.3 2" fill="none" stroke="#333"/></svg>City</li><li><svg viewBox="0 0 8 8"><rect x=".5" y=".5" width="7" height="7" fill="none" stroke="#333"/><path d="M1.8 4l1.5 1.5L6.3 2" fill="none" stroke="#333"/></svg>State</li><li><svg viewBox="0 0 8 8"><rect x=".5" y=".5" width="7" height="7" fill="none" stroke="#333"/><path d="M1.8 4l1.5 1.5L6.3 2" fill="none" stroke="#333"/></svg>Zip</li></ul></li>
    </ul>
    <h1 class="headline">Are You Paying Too Much for Auto Insurance? If I Cannot Save You Money On Your Auto and Home Insurance, Then I Will Give You $25 Just For Calling in For a Quote!</h1>
    <p class="intro">Mygoal is to keep my clients' premiums as low as possible without sacrificing coverage in addition to giving exceptional service. People who switch HIAhave saved on average of $446 annually in the state of Florida! Below is a sample auto quote based on public information. Please call us at 407-555-0182 to discuss your specific driver, vehicle, and coverage information.</p>
    <h2 class="premium-title">YOUR MONTHLY ESTIMATED<br>PREMIUM</h2>
    <h2 class="driver">DRIVER: FULLNAME</h2>
    <div class="promo-art" role="img" aria-label="Savings illustration: a house plus a yellow car, 'Savings – Combine and Save! Switch your home and car to HIA today to take advantage of additional discounts'"></div>
    <div class="quote-table" style="top:440px">
      <div class="thead auto-grid"><span>Coverages</span><span>Coverage Limits</span><span>Vehicle1</span></div>
      <div class="row auto-grid"><span>Bodily Injury</span><span>BI1</span><span>BIPrem1</span></div>
      <div class="row auto-grid"><span>Property Damage</span><span>PD1</span><span>PDPrem1</span></div>
      <div class="row auto-grid"><span>Medial Payments</span><span>Medical1</span><span>MedicalPrem1</span></div>
      <div class="row auto-grid"><span>Collision</span><span>Coll1</span><span>CollDed1</span></div>
      <div class="row auto-grid"><span>Medial Payments</span><span>Medical1</span><span>MedicalPrem1</span></div>
      <div class="row auto-grid" style="height:30px"><span>Comprehensive</span><span>Comp1</span><span>CompDed1</span></div>
      <div class="row auto-grid bold"><span></span><span>Premium</span><span>Premium</span></div>
    </div>
    <div class="six-month"><span class="label">Six Month<br>Estimated Premium</span><span class="val"><b>Premium</b>With Taxes and<br>Surcharges</span></div>
    <p class="disclaimer">Premium amounts shown are for a new six month policy and are for illustration only. Your actual premium will vary depending on a variety of factors that may include, but are not necessarily limited to, the coverage and deductible you select, eligibility requirements, credit history, driving record, applicable discounts, vehicle type and characteristics, and the number of miles driven annually. Coverage and discounts subject to terms, qualifications and availability. Insurance policies are not packaged. Each policy is separate and has its own limitations and restrictions. This quote is not a contract or binder of insurance. To apply for insurance you must complete the application process. Your actual premium may be high or lower depending on actual coverage selections. $25 total will only be given to the individual receiving quote if they did not see any savings on their home and auto insurance from their current insurance policies. <span class="last">You must bring your current declarations pages in to the office to collect the $25 for proof of no savings.</span></p>
    <p class="opt-out">If you no longer wish to receive mail solicitations from HIA, please call 407-555-0182</p>
    <footer class="footer">
      <div class="call">CALL US<span>407-555-0182</span></div>
      <svg class="bar" viewBox="0 0 402 46" aria-hidden="true"><path d="M0 0H402V46H14Z" fill="var(--dark)"/></svg>
      <div class="web"><svg class="icon" viewBox="0 0 12 12"><circle cx="6" cy="6" r="5.2" fill="none" stroke="#fff"/><ellipse cx="6" cy="6" rx="2.3" ry="5.2" fill="none" stroke="#fff"/><path d="M.8 6h10.4M1.6 3.5h8.8M1.6 8.5h8.8" stroke="#fff" stroke-width=".8"/></svg>harborinsagency.com</div>
      <div class="addr"><svg class="icon" viewBox="0 0 12 12"><path d="M6 11.5C3 7.8 2 6 2 4.4a4 4 0 018 0C10 6 9 7.8 6 11.5z" fill="#fff"/><circle cx="6" cy="4.3" r="1.5" fill="var(--dark)"/></svg><span>1820 Lakeview Pkwy<br>#210 Orlando, FL 32801</span></div>
    </footer>
  </section>

  <!-- Back: home quote -->
  <section class="page page-home" aria-label="Home insurance quote letter">
    <svg class="header-shape" viewBox="0 0 630 100" aria-hidden="true"><path d="M0 0H630V35H430C360 35 340 95 270 95H0Z" fill="var(--dark)"/></svg>
    <div class="agency-name"><span class="initials">HIA</span><span class="full">HARBOR INSURANCE AGENCY</span></div>
    <div class="contact" style="top:52px">
      <p>Sample Auto Insurance Quote<br>¡Hablamos Español!</p>
      <p>Harbor Insurance Agency, Inc.<br>Orlando, FL<br>407-555-0182<br>DReyes@keystonecover.com<br>HarborInsAgency.com</p>
    </div>
    <ul class="fields" style="top:108px">
      <li><ul><li><svg viewBox="0 0 8 8"><rect x=".5" y=".5" width="7" height="7" fill="none" stroke="#333"/><path d="M1.8 4l1.5 1.5L6.3 2" fill="none" stroke="#333"/></svg>FullName</li><li><svg viewBox="0 0 8 8"><rect x=".5" y=".5" width="7" height="7" fill="none" stroke="#333"/><path d="M1.8 4l1.5 1.5L6.3 2" fill="none" stroke="#333"/></svg>Address</li><li><svg viewBox="0 0 8 8"><rect x=".5" y=".5" width="7" height="7" fill="none" stroke="#333"/><path d="M1.8 4l1.5 1.5L6.3 2" fill="none" stroke="#333"/></svg>Address2</li></ul></li>
      <li><ul><li><svg viewBox="0 0 8 8"><rect x=".5" y=".5" width="7" height="7" fill="none" stroke="#333"/><path d="M1.8 4l1.5 1.5L6.3 2" fill="none" stroke="#333"/></svg>City</li><li><svg viewBox="0 0 8 8"><rect x=".5" y=".5" width="7" height="7" fill="none" stroke="#333"/><path d="M1.8 4l1.5 1.5L6.3 2" fill="none" stroke="#333"/></svg>State</li><li><svg viewBox="0 0 8 8"><rect x=".5" y=".5" width="7" height="7" fill="none" stroke="#333"/><path d="M1.8 4l1.5 1.5L6.3 2" fill="none" stroke="#333"/></svg>Zip</li></ul></li>
    </ul>
    <p class="pitch">If you are tired of paying too much for Home Insurance and wantall your insurance needs handled under one agency,then call us at <b>407-555-0182.</b> One call is all it takes to see if you've got the right coverage at the right price.</p>
    <div class="example-band">BELOW IS AN EXAMPLE OF A RECENT HOME INSURANCE POLICY IN ORLANDO</div>
    <div class="home-facts"><span>Year Built: 2015</span><span style="font-weight:500">4 Bedrooms</span><span>Heated Square Feet: 2568</span></div>
    <div class="quote-table home-table">
      <div class="thead home-grid"><span>CoverageLimit</span><span></span></div>
      <div class="row home-grid"><span>A - Dwelling Protection</span><span>$305,000.00</span></div>
      <div class="row home-grid"><span>B - Other Structures</span><span>6,100.00</span></div>
      <div class="row home-grid"><span>C - Personal Property</span><span>106,750.00</span></div>
      <div class="row home-grid"><span>D - Loss of Use</span><span>30,500.00</span></div>
      <div class="row home-grid"><span>E - Personal Liability</span><span>$300,000</span></div>
      <div class="row home-grid"><span>F - Medical Protection</span><span>$1,000.00</span></div>
      <div class="row home-grid"><span>AOP Deductible</span><span>$2,500</span></div>
      <div class="row home-grid"><span>Hurricane&nbsp; Deductible</span><span>2%</span></div>
    </div>
    <p class="quote-note">The quoted premium is a sample premium based on a recent policy purchased in Orlando. Premium will differ based on information obtained on your application.</p>
    <p class="sign-off">Sincerely,</p>
    <div class="signature" role="img" aria-label="Handwritten signature of Daniel Reyes"></div>
    <p class="signer">Daniel Reyes<br>Agency Principal</p>
    <svg class="burst" viewBox="0 0 190 190" aria-hidden="true"><path fill="var(--dark)" d="M95 8L104 45 126 14 124 52 157 30 141 64 180 56 152 82 188 95 152 108 180 134 141 126 157 160 124 138 126 176 104 145 95 182 86 145 64 176 66 138 33 160 49 126 10 134 38 108 2 95 38 82 10 56 49 64 33 30 66 52 64 14 86 45Z"/></svg>
    <div class="burst-text"><small>Total Annual<br>Premium</small><strong>$725.00</strong></div>
    <div class="roof-note"><h3>Newer Roof,<br>Save Even More.</h3>If you have a newer roof,you May qualify for added Savings on your Keystone homeowners insurance.<b>Ask me today!</b></div>
    <footer class="footer">
      <div class="call">CALL US<span>407-555-0182</span></div>
      <svg class="bar" viewBox="0 0 402 46" aria-hidden="true"><path d="M0 0H402V46H14Z" fill="var(--dark)"/></svg>
      <div class="web"><svg class="icon" viewBox="0 0 12 12"><circle cx="6" cy="6" r="5.2" fill="none" stroke="#fff"/><ellipse cx="6" cy="6" rx="2.3" ry="5.2" fill="none" stroke="#fff"/><path d="M.8 6h10.4M1.6 3.5h8.8M1.6 8.5h8.8" stroke="#fff" stroke-width=".8"/></svg>harborinsagency.com</div>
      <div class="addr"><svg class="icon" viewBox="0 0 12 12"><path d="M6 11.5C3 7.8 2 6 2 4.4a4 4 0 018 0C10 6 9 7.8 6 11.5z" fill="#fff"/><circle cx="6" cy="4.3" r="1.5" fill="var(--dark)"/></svg><span>1820 Lakeview Pkwy<br>#210 Orlando, FL 32801</span></div>
    </footer>
  </section>

</main>
</body>
</html>
```